タイトル 「週末ガーデナーのための水やり流・花咲かせ節約術」
サブタイトル 「毎日が楽になる5つの習慣」

上記の表紙デザインをお願いします。基本お任せします。
本の内容  原稿を添付します。

その他ご不明な点がございましたらお気楽にご質問ください。よろしくお願いいたします。
著者名 星空ナビゲーター 森川佳代 from神戸

本の内容とよくマッチしたデザインだと思いました。インパクトもあり本の対象であるアラフォーの好みと合っているように思いました。

沢山のご応募ありがとうございました。何もかもか初めての作業で、不安でしたが、関心を持っていただいて心からありがたく思っております。これからも電子書籍の出版を考えております。ご縁がありましたらまた、今後もよろしくお願いします。
ありがとうございました。

```html
<!DOCTYPE html>
<html lang="ja">
<head>
<meta charset="utf-8">
<title>週末ガーデナーのための水やり流・花咲かせ節約術</title>
<link href="https://fonts.googleapis.com/css2?family=M+PLUS+Rounded+1c:wght@500;700;800&family=Noto+Sans+JP:wght@400;500;700&display=swap" rel="stylesheet">
<style>
  :root {
    --gold: #e8b54c;
    --gold-light: #efc468;
    --gold-deep: #d9a23a;
    --pink: #e6478c;
    --ink: #2a2a2a;
    --white: #ffffff;
    --frame: #e3c07a;
  }
  * { margin: 0; padding: 0; box-sizing: border-box; }
  html, body { width: 849px; height: 1200px; overflow: hidden; background: var(--white); }
  .cover {
    position: relative;
    width: 849px;
    height: 1200px;
    overflow: hidden;
    font-family: "Noto Sans JP", sans-serif;
  }
  .pattern-field {
    position: absolute;
    inset: 0;
    background: radial-gradient(circle at 50% 35%, var(--gold-light) 0%, var(--gold) 55%, var(--gold-deep) 100%);
  }
  .silhouette {
    position: absolute;
    left: 330px;
    top: 28px;
    width: 190px;
    height: 250px;
    background: linear-gradient(180deg, #fff8ea 0%, #fbeed2 100%);
    border-radius: 48% 48% 12% 12% / 40% 40% 10% 10%;
    opacity: 0.92;
  }
  .title-panel {
    position: absolute;
    left: 156px;
    top: 265px;
    width: 537px;
    height: 392px;
    background: var(--white);
    border-radius: 34px;
    box-shadow: 0 0 0 5px rgba(255,255,255,0.45);
    text-align: center;
  }
  .title-lead {
    position: absolute;
    left: 0; right: 0;
    top: 38px;
    font-family: "M PLUS Rounded 1c", sans-serif;
    font-weight: 500;
    font-size: 28px;
    letter-spacing: 1px;
    color: var(--pink);
  }
  .title-rule {
    position: absolute;
    left: 118px;
    right: 118px;
    top: 88px;
    height: 2px;
    background: var(--frame);
  }
  .title-main {
    position: absolute;
    left: 0; right: 0;
    top: 118px;
    font-family: "M PLUS Rounded 1c", sans-serif;
    font-weight: 700;
    font-size: 64px;
    line-height: 92px;
    color: var(--pink);
    letter-spacing: 2px;
  }
  .subtitle {
    position: absolute;
    left: 0; right: 0;
    top: 710px;
    text-align: center;
    font-family: "M PLUS Rounded 1c", sans-serif;
    font-weight: 700;
    font-size: 44px;
    color: var(--white);
    letter-spacing: 2px;
  }
  .subtitle .count {
    position: relative;
    display: inline-block;
    font-size: 96px;
    line-height: 1;
    font-weight: 800;
    vertical-align: -12px;
    margin: 0 2px;
  }
  .subtitle .spark {
    position: absolute;
    left: 50%;
    top: -40px;
    width: 90px;
    height: 44px;
    transform: translateX(-50%);
  }
  .author-band {
    position: absolute;
    left: 0;
    top: 826px;
    width: 849px;
    height: 234px;
    background: var(--white);
    text-align: center;
    color: var(--ink);
  }
  .author-role {
    margin-top: 72px;
    font-weight: 700;
    font-size: 34px;
    letter-spacing: 1px;
  }
  .author-name {
    margin-top: 6px;
    font-weight: 500;
    font-size: 32px;
    letter-spacing: 2px;
  }
  .author-home {
    margin-top: 2px;
    font-size: 20px;
    font-weight: 400;
  }
</style>
</head>
<body>
<div class="cover">
  <div class="pattern-field" role="img" aria-label="金色の地に装飾タイル模様"></div>
  <div class="silhouette" role="img" aria-label="髪を結い上げた女性の横顔シルエット"></div>

  <div class="title-panel">
    <p class="title-lead">週末ガーデナーのための</p>
    <div class="title-rule"></div>
    <h1 class="title-main">水やり流<br>花咲かせ節約術</h1>
  </div>

  <p class="subtitle">毎日が楽になる<span class="count"><svg class="spark" viewBox="0 0 90 44" aria-hidden="true"><g stroke="#ffffff" stroke-width="3" stroke-linecap="round"><line x1="45" y1="4" x2="45" y2="26"/><line x1="22" y1="12" x2="32" y2="30"/><line x1="68" y1="12" x2="58" y2="30"/><line x1="4" y1="28" x2="20" y2="36"/><line x1="86" y1="28" x2="70" y2="36"/></g></svg>5</span>つの習慣</p>

  <div class="author-band">
    <p class="author-role">星空ナビゲーター</p>
    <p class="author-name">森川佳代</p>
    <p class="author-home">from神戸</p>
  </div>
</div>
</body>
</html>
```